Fixed price car insurance banner ad for insurance broker

We need a banner ad for addition to web pages and which will advertise an innovative insurance product we are selling.

We are an insurance broker and our product is a fixed price car insurance product.

The banner ad needs to display the company logo. This will be uploaded within the file upload section.

The remainder of the banner ad needs to explain what we are offering and also include the gear stick picture for impact.

We would like to see colours that tie in with the corporate colours, or alternative are striking and have presence on even the busiest web page I.e. Black banner and silver / white text. Please see the file upload for a sample of the brochure we are preparing for this product.

Target Market(s)

Private and commercial clients with both regular and high value motor vehicles.

Industry/Entity Type

Car Insurance

Font styles to use
Serif
Sans Serif

Colors

Designer to choose colors to be used in the design.

Requirements
Must have
• The banner must have the company logo on both pages.

I would like the advert to scroll / roll / fade or other between two pages displaying the following text:

Page 1
"Motor Insurance Scheme"
"Anything But Standard"
and including the gear knob picture

Page 2
Any Driver, Any Car, No Forms and One Flat Premium*

On clicking the banner ad, this will open an email, pre populated with email contact to request more detail.

Nice to have
• Open to your suggestions on this
Should not have
• Nothing at this stage. I will guide you when the ads are being submitted.

```html
<!DOCTYPE html>
<html lang="en">
<head>
<meta charset="UTF-8">
<title>Harwell Insurance – Motor Insurance Scheme</title>
<link rel="stylesheet" href="https://fonts.googleapis.com/css2?family=Tinos:wght@400&display=swap">
<style>
  :root {
    --logo-bg: #ffffff;
    --logo-ink: #1d2d63;
    --band-black: #000000;
    --band-steel: #2a3346;
    --headline: #f4f4f4;
    --headline-shadow: rgba(120, 140, 190, 0.55);
    --knob-light: #d9dde6;
    --knob-mid: #6b80b3;
    --knob-dark: #1a2652;
  }
  * { box-sizing: border-box; margin: 0; padding: 0; }
  html, body { width: 1200px; height: 148px; overflow: hidden; background: var(--band-black); }
  .banner {
    position: relative;
    width: 1200px;
    height: 148px;
    overflow: hidden;
    background:
      linear-gradient(90deg, var(--band-steel) 0, var(--band-black) 190px),
      var(--band-black);
    font-family: "Tinos", "Times New Roman", serif;
  }
  .brand {
    position: absolute;
    left: 0; top: 0;
    width: 297px; height: 148px;
    background: var(--logo-bg);
    display: flex;
    flex-direction: column;
    align-items: center;
    justify-content: center;
    color: var(--logo-ink);
    font-weight: 400;
    line-height: 1;
  }
  .brand-name { font-size: 50px; letter-spacing: 6px; }
  .brand-sub { font-size: 25px; letter-spacing: 8px; margin-top: 14px; }
  .headline {
    position: absolute;
    right: 360px;
    color: var(--headline);
    font-weight: 400;
    font-size: 48px;
    line-height: 1;
    white-space: nowrap;
    text-shadow: 2px 2px 3px var(--headline-shadow);
  }
  .headline-top { top: 14px; }
  .headline-bottom { top: 76px; }
  .gear-knob {
    position: absolute;
    left: 1005px; top: -17px;
    width: 182px; height: 182px;
    border-radius: 50%;
    background: radial-gradient(circle at 50% 40%, var(--knob-light) 0, var(--knob-mid) 55%, var(--knob-dark) 100%);
  }
</style>
</head>
<body>
  <div class="banner">
    <div class="brand">
      <span class="brand-name">HARWELL</span>
      <span class="brand-sub">INSURANCE</span>
    </div>
    <h1 class="headline headline-top">Motor Insurance Scheme</h1>
    <p class="headline headline-bottom">Anything But Standard</p>
    <div class="gear-knob" role="img" aria-label="Gear knob showing a five-speed shift pattern with reverse"></div>
  </div>
</body>
</html>
```